Business Card design for a company called Tallow Flame NI

I need a business card design for my oil fired boiler servicing company. I have a logo design already and Im just looking that incorporated into the business card design. card details; Tallow Flame NI
Oil Burner Servicing - Mid Ulster Area
Service Engineer - Owen Marsh
Mobile 07751364927
email - Tallow.Flame.NI@hearthmail.example
www.tallowflameni.example
I carry out Servicing, Commissioning, Fault Finding, Warranty Validation
Target Market(s)
home owners with oil fired central heating
Industry/Entity Type
Business
Contact Information for Business Card
Tallow Flame NI
Tell. 07751364927
Web: www.tallowflameni.example
email Tallow.Flame.NI@Hearthmail.Example
Servicing Fault Finding Commissioning Warranty Validation
Look and feel

```html
<!DOCTYPE html>
<html lang="en">
<head>
<meta charset="utf-8">
<title>Tallow Flame NI – Business Card</title>
<link href="https://fonts.googleapis.com/css2?family=Open+Sans:ital,wght@0,400;0,600;0,700;1,400&display=swap" rel="stylesheet">
<style>
  :root {
    --bg: #ece8e1;
    --white: #ffffff;
    --green-deep: #2fa83f;
    --green-mid: #45b649;
    --green-light: #7cc94a;
    --lime: #c9dc2a;
    --brand-green: #4cb848;
    --ink-soft: rgba(255,255,255,0.92);
  }
  * { margin: 0; padding: 0; box-sizing: border-box; }
  html, body {
    width: 1200px; height: 950px; overflow: hidden;
    background: var(--bg);
    font-family: "Open Sans", Arial, sans-serif;
  }
  .canvas { position: relative; width: 1200px; height: 950px; }

  .card {
    position: absolute;
    width: 620px; height: 355px;
    border-radius: 4px;
    overflow: hidden;
    box-shadow: 0 10px 28px rgba(0,0,0,0.18);
  }

  /* Front card */
  .card-front { left: 90px; top: 80px; background: var(--white); }
  .front-top { position: absolute; inset: 0 0 auto 0; height: 160px; background: var(--white); }
  .front-bottom {
    position: absolute; left: 0; right: 0; bottom: 0; height: 195px;
    background: linear-gradient(160deg, var(--green-light) 0%, var(--green-mid) 45%, var(--green-deep) 100%);
  }
  .brand-mark {
    position: absolute; left: 150px; top: 126px;
    width: 68px; height: 68px; border-radius: 50%;
    background: var(--brand-green);
    border: 5px solid var(--white);
  }
  .brand-block { position: absolute; left: 232px; top: 92px; }
  .brand-name {
    font-weight: 700; font-size: 36px; line-height: 1;
    color: var(--brand-green); letter-spacing: -0.5px;
  }
  .brand-tagline {
    margin-top: 6px;
    font-size: 9px; font-weight: 600; letter-spacing: 1.6px;
    text-transform: uppercase; color: var(--brand-green);
  }
  .person { position: absolute; left: 44px; top: 200px; color: var(--white); }
  .person-name { font-weight: 600; font-size: 24px; line-height: 1.1; }
  .person-role { font-size: 15px; margin-top: 2px; color: var(--ink-soft); }
  .contacts {
    position: absolute; left: 250px; top: 212px;
    list-style: none; color: var(--white); font-size: 14px;
  }
  .contacts li { display: flex; align-items: center; gap: 10px; height: 25px; }
  .contacts svg { width: 14px; height: 14px; flex: none; }

  /* Back card */
  .card-back {
    left: 490px; top: 500px;
    background: linear-gradient(150deg, var(--green-light) 0%, var(--green-mid) 50%, var(--green-deep) 100%);
  }
  .back-decoration-area {
    position: absolute; right: 0; top: 0;
    width: 340px; height: 170px;
    background: linear-gradient(200deg, rgba(201,220,42,0.55) 0%, rgba(124,201,74,0.25) 55%, rgba(124,201,74,0) 100%);
  }
  .back-text { position: absolute; left: 60px; top: 190px; color: var(--white); }
  .back-name { font-weight: 700; font-size: 34px; line-height: 1; letter-spacing: -0.3px; }
  .back-tagline {
    margin-top: 6px; font-size: 8.5px; font-weight: 600;
    letter-spacing: 1.5px; text-transform: uppercase;
  }
  .services { margin-top: 12px; font-style: italic; font-size: 17px; line-height: 1.35; }
</style>
</head>
<body>
<div class="canvas">

  <section class="card card-front" aria-label="Business card front">
    <div class="front-top"></div>
    <div class="front-bottom"></div>
    <div class="brand-mark" aria-hidden="true"></div>
    <div class="brand-block">
      <div class="brand-name">Tallow Flame NI</div>
      <div class="brand-tagline">Oil Burner Servicing - Mid Ulster Area</div>
    </div>
    <div class="person">
      <div class="person-name">Owen Marsh</div>
      <div class="person-role">Service Engineer</div>
    </div>
    <ul class="contacts">
      <li>
        <svg viewBox="0 0 14 14" aria-hidden="true"><rect x="3.5" y="0.8" width="7" height="12.4" rx="1.2" fill="none" stroke="#fff" stroke-width="1.4"/><circle cx="7" cy="11" r="0.8" fill="#fff"/></svg>
        07751364927
      </li>
      <li>
        <svg viewBox="0 0 14 14" aria-hidden="true"><path d="M3 1.5l2.2 2.5-1.2 1.6c.8 1.7 2 2.9 3.6 3.7l1.6-1.2 2.5 2.2-1.3 2c-4.6-.4-8.5-4.3-8.9-8.9z" fill="#fff"/></svg>
        07751364927
      </li>
      <li>
        <svg viewBox="0 0 14 14" aria-hidden="true"><rect x="1" y="3" width="12" height="8.5" rx="1" fill="#fff"/><path d="M1.5 3.6L7 8l5.5-4.4" fill="none" stroke="#3aae45" stroke-width="1.2"/></svg>
        Tallow.Flame.NI@hearthmail.example
      </li>
      <li>
        <svg viewBox="0 0 14 14" aria-hidden="true"><circle cx="7" cy="7" r="6" fill="none" stroke="#fff" stroke-width="1.3"/><ellipse cx="7" cy="7" rx="2.6" ry="6" fill="none" stroke="#fff" stroke-width="1.1"/><path d="M1 7h12" stroke="#fff" stroke-width="1.1"/></svg>
        www.tallowflameni.example
      </li>
    </ul>
  </section>

  <section class="card card-back" aria-label="Business card back">
    <div class="back-decoration-area" role="img" aria-label="Area for the yellow-green decorative artwork"></div>
    <div class="back-text">
      <div class="back-name">Tallow Flame NI</div>
      <div class="back-tagline">Oil Burner Servicing - Mid Ulster Area</div>
      <div class="services">Commissioning | Fault Finding<br>Warranty Validation</div>
    </div>
  </section>

</div>
</body>
</html>
```